Flyer Design Project

We are offering a new class on cyber crime and want to advertise this course to students. We would like to see a design that is eye catching and coveys the goals of the course, when it meets and a brief abstract for the class.

The course will focus on the economics of cyber crime so including one or two graphics that get across this point would be good.

Requirements
Must have
• Course name "Cyber Crime"
Call number "CS 795 - 004"
Course meeting time (day of week and time) Tue. 4:30-7:10pm
Course goals
Course abstract

```html
<!DOCTYPE html>
<html lang="en">
<head>
<meta charset="utf-8">
<title>Cyber Crime – Course Flyer Variations</title>
<link rel="stylesheet" href="https://fonts.googleapis.com/css2?family=Jost:wght@400;500;700;800;900&display=swap">
<style>
  :root {
    --canvas-bg: #ffffff;
    --text-light: #ffffff;

    --blue-hero-a: #0b2f73;
    --blue-hero-b: #2f7fd0;
    --blue-hero-c: #9fd2f4;
    --blue-panel: #3aa9de;
    --blue-footer: #1f5597;

    --green-hero-a: #0f4d17;
    --green-hero-b: #46a83c;
    --green-hero-c: #c9ecb9;
    --green-panel: #000000;
    --green-footer: #4cae47;

    --red-hero-a: #6a0b0e;
    --red-hero-b: #d52a2c;
    --red-hero-c: #f6b3a8;
    --red-panel: #474645;
    --red-footer: #d9272b;
  }

  * { box-sizing: border-box; margin: 0; padding: 0; }

  html, body {
    width: 1200px;
    height: 574px;
    overflow: hidden;
    background: var(--canvas-bg);
  }

  .canvas {
    position: relative;
    width: 1200px;
    height: 574px;
    font-family: "Jost", "Futura", sans-serif;
    color: var(--text-light);
  }

  .flyer {
    position: absolute;
    top: 53px;
    width: 370px;
    height: 475px;
    display: flex;
    flex-direction: column;
    overflow: hidden;
  }
  .flyer--blue  { left: 24px;  --hero-a: var(--blue-hero-a);  --hero-b: var(--blue-hero-b);  --hero-c: var(--blue-hero-c);  --panel: var(--blue-panel);  --footer: var(--blue-footer); }
  .flyer--green { left: 415px; --hero-a: var(--green-hero-a); --hero-b: var(--green-hero-b); --hero-c: var(--green-hero-c); --panel: var(--green-panel); --footer: var(--green-footer); }
  .flyer--red   { left: 810px; --hero-a: var(--red-hero-a);   --hero-b: var(--red-hero-b);   --hero-c: var(--red-hero-c);   --panel: var(--red-panel);   --footer: var(--red-footer); }

  .flyer__hero {
    position: relative;
    height: 205px;
    flex: none;
  }
  .flyer__hero-art {
    position: absolute;
    inset: 0;
    background:
      radial-gradient(ellipse 60% 45% at 55% 60%, var(--hero-c) 0%, transparent 70%),
      linear-gradient(160deg, var(--hero-a) 0%, var(--hero-b) 55%, var(--hero-a) 100%);
  }
  .flyer__title {
    position: absolute;
    top: 9px;
    left: 0;
    right: 0;
    text-align: center;
    font-weight: 900;
    font-size: 66px;
    line-height: 0.8;
    letter-spacing: -2px;
    text-transform: uppercase;
    transform: scaleX(0.88);
    color: var(--text-light);
  }

  .flyer__panel {
    flex: 1;
    min-height: 0;
    overflow: hidden;
    background: var(--panel);
    padding: 12px 28px 0;
    text-align: center;
  }
  .flyer__heading {
    font-weight: 700;
    font-size: 12.5px;
    line-height: 1.2;
    margin-bottom: 5px;
  }
  .flyer__goals {
    list-style: none;
    font-size: 9px;
    line-height: 1.2;
    padding: 0 22px;
    margin-bottom: 10px;
  }
  .flyer__goals li { margin-bottom: 7px; }
  .flyer__goals b { font-weight: 700; font-size: 10px; margin-right: 2px; }
  .flyer__abstract {
    font-size: 9px;
    line-height: 1.42;
  }

  .flyer__footer {
    flex: none;
    height: 50px;
    background: var(--footer);
    display: flex;
    align-items: center;
    justify-content: space-between;
    padding: 0 10px;
    font-weight: 800;
    font-size: 10.4px;
    white-space: nowrap;
  }
</style>
</head>
<body>
<main class="canvas">

  <article class="flyer flyer--blue">
    <div class="flyer__hero">
      <div class="flyer__hero-art" role="img" aria-label="Streams of binary code over rows of blue dollar signs"></div>
      <h1 class="flyer__title">Cyber<br>Crime</h1>
    </div>
    <section class="flyer__panel">
      <h2 class="flyer__heading">COURSE GOALS:</h2>
      <ol class="flyer__goals">
        <li><b>1)</b> Understand how modern cyber-crime operates on a technical and economic level</li>
        <li><b>2)</b> Analyze some of the potential places to intervene at an economic, technical and policy level.</li>
      </ol>
      <h2 class="flyer__heading">COURSE ABSTRACT:</h2>
      <p class="flyer__abstract">Arguably the single most significant change in the cyber-security landscape has been the explosive rise of profit-fueled cyber-crime. Obtaining a detailed, structural understanding of how profit-driven cyber crime works — its underlying economics and associated business practices — has the potential to illuminate new defensive measures that might prove far more efficient for countering attacks than purely technical measures. This research seminar will delve into our current understanding of the economics of cyber-crime.</p>
    </section>
    <footer class="flyer__footer">
      <span>COURSE: CS 795 - 004</span><span>DAY: TUESDAY</span><span>TIME: 4:30 PM-7:10PM</span>
    </footer>
  </article>

  <article class="flyer flyer--green">
    <div class="flyer__hero">
      <div class="flyer__hero-art" role="img" aria-label="Streams of binary code over rows of green dollar signs"></div>
      <h1 class="flyer__title">Cyber<br>Crime</h1>
    </div>
    <section class="flyer__panel">
      <h2 class="flyer__heading">COURSE GOALS:</h2>
      <ol class="flyer__goals">
        <li><b>1)</b> Understand how modern cyber-crime operates on a technical and economic level</li>
        <li><b>2)</b> Analyze some of the potential places to intervene at an economic, technical and policy level.</li>
      </ol>
      <h2 class="flyer__heading">COURSE ABSTRACT:</h2>
      <p class="flyer__abstract">Arguably the single most significant change in the cyber-security landscape has been the explosive rise of profit-fueled cyber-crime. Obtaining a detailed, structural understanding of how profit-driven cyber crime works — its underlying economics and associated business practices — has the potential to illuminate new defensive measures that might prove far more efficient for countering attacks than purely technical measures. This research seminar will delve into our current understanding of the economics of cyber-crime.</p>
    </section>
    <footer class="flyer__footer">
      <span>COURSE: CS 795 - 004</span><span>DAY: TUESDAY</span><span>TIME: 4:30 PM-7:10PM</span>
    </footer>
  </article>

  <article class="flyer flyer--red">
    <div class="flyer__hero">
      <div class="flyer__hero-art" role="img" aria-label="Streams of binary code over rows of red dollar signs"></div>
      <h1 class="flyer__title">Cyber<br>Crime</h1>
    </div>
    <section class="flyer__panel">
      <h2 class="flyer__heading">COURSE GOALS:</h2>
      <ol class="flyer__goals">
        <li><b>1)</b> Understand how modern cyber-crime operates on a technical and economic level</li>
        <li><b>2)</b> Analyze some of the potential places to intervene at an economic, technical and policy level.</li>
      </ol>
      <h2 class="flyer__heading">COURSE ABSTRACT:</h2>
      <p class="flyer__abstract">Arguably the single most significant change in the cyber-security landscape has been the explosive rise of profit-fueled cyber-crime. Obtaining a detailed, structural understanding of how profit-driven cyber crime works — its underlying economics and associated business practices — has the potential to illuminate new defensive measures that might prove far more efficient for countering attacks than purely technical measures. This research seminar will delve into our current understanding of the economics of cyber-crime.</p>
    </section>
    <footer class="flyer__footer">
      <span>COURSE: CS 795 - 004</span><span>DAY: TUESDAY</span><span>TIME: 4:30 PM-7:10PM</span>
    </footer>
  </article>

</main>
</body>
</html>
```